RVM Flooring Flyer/Direct Mail

I need a flyer that will be distributed by letterboxing. this flyer will be offering free measure and quotes for supply and installation of timber, bamboo, and laminate flooring. The flyer will need to eye catching and professional looking.
The main purpose of the flyer is to generate appointments that will be followed up by a sales measure and quote team.

- Free Measure and Quote
Services:
- Remove and dispose of old floor coverings
- Pre installation floor repair
- New floor installation
- Free dust and clean on every new floor installation

I have some design files, logo and stock images, the flyer must not clash with the logo and business card.

You can use any image from Pextra Images as I have subscription with them.
https://images.pextrafoto.com/au/gallery

Here are the links to the Timber and Bamboo flooring supplier that I will be buying from and the third link is for the laminate flooring supplier. Note, this is for getting an idea of what products we will be supplying and installing, Do not use their images!

https://www.grainhaven.com.au/timber-flooring/
https://cantorvex.com.au/bamboo-flooring/
http://www.dalvorsurfaces.com.au/brands/tenmark-laminate/

Target Market(s)

Domestic home owners

Industry/Entity Type

Construction Company

Colors

Designer to choose colors to be used in the design.

Requirements
Must have
• Size: A6 or DL
Nice to have
• Timber: Spotted Gum, Eastern States Blackbutt, Jarrah, Marri, and a large collection of French Oak.
• Bamboo: Our Bamboo range of flooring is engineered to withstand the extremes of the Australian climate.
• Laminate: All our laminate range comes with a 25 year product warranty. Choose from a large range of patterns, colours and finishes.

```html
<!DOCTYPE html>
<html lang="en">
<head>
<meta charset="utf-8">
<title>RVM Flooring – DL Flyer</title>
<link rel="stylesheet" href="https://fonts.googleapis.com/css2?family=Montserrat:wght@400;500;600;700&display=swap">
<style>
  :root{
    --ink:#151515;
    --paper:#ffffff;
    --mist:#dde1ec;
    --mist-soft:#eef0f6;
    --text:#2b2b2b;
    --stage:#e9e7e3;
    --wood-dark:#3b3b3d;
    --wood-mid:#a6784f;
    --wood-light:#d9b27a;
  }
  *{box-sizing:border-box;margin:0;padding:0}
  html,body{width:1200px;height:750px;overflow:hidden}
  body{background:var(--stage);font-family:"Montserrat",sans-serif;color:var(--text);position:relative}

  .flyer{position:absolute;top:25px;width:340px;height:700px;background:var(--paper);overflow:hidden;box-shadow:0 4px 18px rgba(0,0,0,.12)}
  .flyer--products{left:230px}
  .flyer--services{left:630px}

  .corner-shape{position:absolute;inset:0;width:100%;height:100%;pointer-events:none}

  .headline{position:absolute;top:22px;left:0;right:0;text-align:center;text-transform:uppercase;white-space:nowrap}
  .headline__lead{font-size:11px;letter-spacing:1.5px;font-weight:500}
  .headline__main{font-size:22px;letter-spacing:2px;font-weight:600;color:var(--ink)}

  .photo{position:absolute}
  .photo--planks{left:16px;top:62px;width:308px;height:190px;background:linear-gradient(135deg,var(--wood-dark) 0%,#4a4647 40%,var(--wood-mid) 70%,#3d3a3b 100%)}
  .photo--dining{left:16px;top:62px;width:212px;height:240px;background:linear-gradient(180deg,#d8d8d8 0%,#bdbdbd 55%,#9c9a9a 100%)}
  .photo--room-a{left:234px;top:62px;width:90px;height:78px;background:linear-gradient(180deg,#e4e4e4,#8d7967)}
  .photo--room-b{left:234px;top:144px;width:90px;height:78px;background:linear-gradient(180deg,#eceff2,#b57a3e)}
  .photo--room-c{left:234px;top:226px;width:90px;height:76px;background:linear-gradient(180deg,#f0eee9,#7a4a26)}

  .brand{display:flex;align-items:center;gap:5px;font-weight:600;text-transform:uppercase;letter-spacing:1px;white-space:nowrap}
  .brand__mark{width:9px;height:9px;border:1.5px solid currentColor}
  .photo--planks .brand{position:absolute;right:10px;bottom:10px;color:#fff;font-size:9px}

  .intro{position:absolute;top:262px;left:30px;right:30px;text-align:center;font-size:8.5px;line-height:1.45;font-weight:500}

  .swatches{position:absolute;top:318px;left:16px;right:16px;display:flex;justify-content:space-between}
  .swatch{width:90px;height:90px;border-radius:50%}
  .swatch--timber{background:radial-gradient(circle at 40% 40%,#e6cda8,#b9733f 70%,#8a3b24)}
  .swatch--bamboo{background:radial-gradient(circle at 45% 45%,#f0c060,#d08d25 80%)}
  .swatch--laminate{background:radial-gradient(circle at 45% 45%,#c7b59c,#8f7b63 80%)}

  .rule{position:absolute;top:420px;left:16px;right:16px;border-top:2px solid var(--ink)}
  .rule--second{top:425px;border-top-width:1px}

  .ranges{position:absolute;top:436px;left:22px;right:22px;font-size:8.5px;line-height:1.4}
  .range{margin-bottom:6px}
  .range__name{font-weight:700;text-transform:uppercase;color:var(--ink)}

  .cta{position:absolute;display:flex;align-items:center;justify-content:center;text-align:center}
  .cta--mist{background:var(--mist);color:var(--ink);font-size:10px;line-height:1.3;letter-spacing:.5px}
  .cta--ink{background:var(--ink);color:#fff}
  .phone{font-size:19px;font-weight:700;letter-spacing:1.5px}

  .flyer--products .cta--mist{left:16px;top:580px;width:308px;height:54px;justify-content:flex-start;padding-left:24px;text-align:left}
  .flyer--products .cta--ink{left:170px;top:612px;width:154px;height:42px}
  .flyer--products .phone{font-size:15px;color:#fff}

  .warranty{position:absolute;left:200px;top:232px;width:56px;height:56px;border-radius:50%;background:var(--ink);border:2px solid #fff;color:#fff;text-align:center;line-height:1;z-index:2;padding-top:9px}
  .warranty__years{display:block;font-size:18px;font-weight:700}
  .warranty__label{display:block;font-size:7px;font-weight:600;margin-top:1px}

  .services{position:absolute;left:16px;right:16px;top:302px;height:144px;background:var(--ink);color:#fff;padding:16px 18px}
  .services__title{font-size:21px;font-weight:600;letter-spacing:1.5px;text-transform:uppercase;margin-bottom:7px}
  .services__list{list-style:none;font-size:9px;line-height:1.5}
  .services__list li::before{content:"";display:inline-block;width:3px;height:3px;background:#fff;margin:0 7px 2px 0}
  .services__list .services__offer{text-transform:uppercase}
  .services .brand{position:absolute;right:16px;bottom:14px;font-size:8.5px}

  .goal{position:absolute;top:462px;left:30px;right:30px;text-align:center;font-size:8.5px;font-weight:600;line-height:1.5;color:var(--ink)}

  .flyer--services .cta--ink{left:16px;top:560px;width:170px;height:60px;font-size:10px;line-height:1.35;letter-spacing:.5px}
  .flyer--services .cta--mist{left:186px;top:585px;width:138px;height:50px}
  .flyer--services .phone{font-size:16px}
</style>
</head>
<body>

<article class="flyer flyer--products">
  <svg class="corner-shape" viewBox="0 0 340 700" aria-hidden="true">
    <polygon points="0,0 120,0 0,40" fill="var(--mist-soft)"/>
    <polygon points="340,0 340,70 250,0" fill="var(--mist-soft)"/>
    <polygon points="0,700 0,560 90,700" fill="var(--mist-soft)"/>
  </svg>
  <h1 class="headline"><span class="headline__lead">The Specialist</span> <span class="headline__main">In Flooring</span></h1>
  <div class="photo photo--planks" role="img" aria-label="Timber flooring planks stacked on a dark background">
    <span class="brand"><span class="brand__mark"></span>RVM Flooring</span>
  </div>
  <p class="intro">At RVM Flooring we specialise in prefinished timber, bamboo and laminate flooring. We strive to provide a friendly, professional experience to all our customers.</p>
  <div class="swatches">
    <div class="swatch swatch--timber" role="img" aria-label="Timber flooring sample"></div>
    <div class="swatch swatch--bamboo" role="img" aria-label="Bamboo flooring sample"></div>
    <div class="swatch swatch--laminate" role="img" aria-label="Laminate flooring sample"></div>
  </div>
  <div class="rule"></div>
  <div class="rule rule--second"></div>
  <div class="ranges">
    <p class="range"><span class="range__name">Timber:</span><br>Spotted Gum, Eastern States Blackbutt, Jarrah, Marri, and a large collection of French Oak.</p>
    <p class="range"><span class="range__name">Bamboo:</span><br>Our Bamboo range of flooring is engineered to withstand the extremes of the Australian climate.</p>
    <p class="range"><span class="range__name">Laminate:</span><br>All our laminate range comes with a 25 year product warranty. Choose from a large range of patterns, colours and finishes.</p>
  </div>
  <div class="cta cta--mist">Call today for your<br>obligations free quote</div>
  <div class="cta cta--ink"><span class="phone">0491 570 110</span></div>
</article>

<article class="flyer flyer--services">
  <svg class="corner-shape" viewBox="0 0 340 700" aria-hidden="true">
    <polygon points="0,0 110,0 0,36" fill="var(--mist-soft)"/>
    <polygon points="340,0 340,90 260,0" fill="var(--mist-soft)"/>
    <polygon points="340,700 340,600 260,700" fill="var(--mist-soft)"/>
  </svg>
  <h1 class="headline"><span class="headline__lead">The Specialist</span> <span class="headline__main">In Flooring</span></h1>
  <div class="photo photo--dining" role="img" aria-label="Dining room with light grey timber floor"></div>
  <div class="photo photo--room-a" role="img" aria-label="Empty room with timber floor"></div>
  <div class="photo photo--room-b" role="img" aria-label="Living area with honey timber floor"></div>
  <div class="photo photo--room-c" role="img" aria-label="Hallway with dark timber floor"></div>
  <div class="warranty"><span class="warranty__years">25</span><span class="warranty__label">year<br>warranty</span></div>
  <section class="services">
    <h2 class="services__title">Our Services</h2>
    <ul class="services__list">
      <li>Remove and dispose of old floor coverings</li>
      <li>Pre installation floor repair</li>
      <li>New floor installation</li>
      <li>Free dust and clean on every new floor installation</li>
      <li class="services__offer">Free measure and quote</li>
    </ul>
    <span class="brand"><span class="brand__mark"></span>RVM Flooring</span>
  </section>
  <p class="goal">Our goal is to provide the highest standard in customer service, integrity, quality and value for money. As a family business we understand the importance of relationship and seek to make your experience one you will be pleased you made.</p>
  <div class="cta cta--ink">Call today for your<br>obligations free quote</div>
  <div class="cta cta--mist"><span class="phone">0491 570 110</span></div>
</article>

</body>
</html>
```